Oral Health Packaging Design

I need to redesign the products in our VELTRIX Range of toothpastes and mouthwash.
1. VELTRIX Toothpaste (http://www.frommelquay.com.au/aus/poise-toothpaste.html)
2. VELTRIX Tongue Gel (http://www.frommelquay.com.au/aus/veltrix-gel.html)
3. VELTRIX (with TORVA R47) "zephyrline" (http://www.frommelquay.com.au/aus/veltrix-powder.html)
4. VELTRIX (with TORVA P63 "dentisafe" (New Product)
5. VELTRIX Poise Rinse (two bottles mixed together) (http://www.frommelquay.com.au/aus/poise-rinse.html)

I need all the products to look like a family.
TOOTHPASTE & MOUTHWASH
The toothpaste and tongue gel are used together. So we are dumping the zephyrline and poise names and rebranding under just VelTrix. Customer feedback is that they are embarrased to put these products in their bathroom in case someone sees them. So we are looking for a clean, corporate and clinical look that emphasises mouth health and maximising fresh breath.
The R47 and P63 can be used together but not necessary. These are our special blend of probiotics. By law we can only say that they treat bad breath, we are not allowed to talk about other health benefits. So I thought that images (maybe as a watermark behind the text might help). So looking to get a graphival look to these labels for the probiotics. Disctinction is that R47 is for fresh breath and P63 is to prevent tooth decay and Oral health
Poise Rinse comes in three strengths. It is two liquides mixed together. This rinse is used twice a week to knock down the bacteria to help the probitocis work

Initial stage is to get the family feel.
Next is the R47 and P63 labels
Next is the Toothpaste
Next is the Poise Rinse
Next is the tongue gel

Target Market(s)

People with bad breath or looking for maximum mouth health

Industry/Entity Type

Health

Requirements
Must have
• Corporate, clinical, neat and tidy should show confidence
Dropping the Zephyrline and Poise labels. Putting everything under VELTRIX brand. However probiotics can have "zephyrline" at bottom of label for R47 and "dentisafe" at bottom of label for P63
Nice to have
• I have uploaded two brochures of R47 and P63. I like the circle design around the R47 and the M18and I also like the colouring.
Should not have
• no medical claims

```html
<!DOCTYPE html>
<html lang="en">
<head>
<meta charset="utf-8">
<title>VELTRIX Oral Care Range</title>
<link rel="stylesheet" href="https://fonts.googleapis.com/css2?family=Montserrat:ital,wght@0,500;0,700;0,800;1,600&family=Oswald:wght@600;700&display=swap">
<style>
  :root{
    --teal:#2bb5c8;
    --pink:#df6a9f;
    --brown:#7b4b3c;
    --pattern-teal:#8a5f57;
    --pattern-pink:#9a5a63;
    --white:#ffffff;
    --cap:#f1f1f1;
    --gold:#d9a640;
    --amber:#6e3a1d;
    --ink:#2b2b2b;
  }
  *{box-sizing:border-box;margin:0;padding:0}
  html,body{width:1200px;height:900px;overflow:hidden;background:var(--white)}
  body{position:relative;font-family:"Montserrat",sans-serif;color:var(--white)}

  /* tubes */
  .tube{position:absolute;top:36px;width:270px;height:544px;border-radius:14px 14px 4px 4px;overflow:hidden}
  .tube--teal{background:var(--teal)}
  .tube--pink{background:var(--pink)}
  .tube__shoulder{position:absolute;left:0;right:0;top:0;height:22px;background:var(--cap)}
  .tube__crimp{position:absolute;left:0;right:0;bottom:0;height:30px;background:var(--cap)}
  .tube__pattern{position:absolute;top:22px;left:0;right:0;height:300px;clip-path:polygon(30% 0,100% 0,100% 100%)}
  .tube--teal .tube__pattern{background:var(--pattern-teal)}
  .tube--pink .tube__pattern{background:var(--pattern-pink)}
  .tube__pattern--back{clip-path:polygon(0 0,100% 0,52% 100%)}
  .seal{position:absolute;top:36px;right:26px;width:42px;height:42px;border-radius:50%;background:var(--gold);border:3px solid var(--white)}

  .brand{position:absolute;left:0;top:200px;background:var(--white);color:var(--brown);font-weight:800;font-size:40px;letter-spacing:-1px;padding:2px 14px 2px 18px}
  .product-name{position:absolute;left:0;top:256px;background:var(--brown);font-family:"Oswald",sans-serif;font-weight:700;font-size:36px;line-height:1.05;padding:8px 18px;text-transform:uppercase}
  .tagline{position:absolute;left:18px;top:360px;font-style:italic;font-weight:600;font-size:14px}
  .features{position:absolute;left:18px;top:392px;font-size:10px;font-weight:700;line-height:1.6;list-style:none;width:150px}
  .net{position:absolute;left:18px;bottom:44px;font-weight:800;font-size:15px}

  .back-copy{position:absolute;left:150px;top:230px;width:100px;font-size:7px;line-height:1.45}
  .back-copy h3{font-size:7.5px;font-weight:800;margin-bottom:4px;text-align:center}

  /* rinse bottles */
  .bottle{position:absolute;top:584px;width:124px;height:280px}
  .bottle__cap{position:absolute;left:20px;top:0;width:84px;height:66px;background:var(--cap);border-radius:14px 14px 4px 4px}
  .bottle__body{position:absolute;left:0;top:60px;width:124px;height:220px;background:var(--cap);border-radius:26px 26px 8px 8px;overflow:hidden}
  .bottle__label{position:absolute;left:0;right:0;top:28px;height:170px}
  .bottle__label--teal{background:var(--teal)}
  .bottle__label--pink{background:var(--pink)}
  .mini-brand{position:absolute;left:0;top:10px;background:var(--white);color:var(--brown);font-weight:800;font-size:19px;padding:1px 8px}
  .mini-name{position:absolute;left:0;top:40px;background:var(--brown);font-family:"Oswald",sans-serif;font-weight:700;font-size:17px;line-height:1.05;padding:4px 8px;text-transform:uppercase}
  .mini-copy{position:absolute;left:8px;top:100px;width:76px;font-size:6px;line-height:1.4}
  .mini-net{position:absolute;left:8px;bottom:10px;font-size:7px;font-weight:700}
  .mini-seal{position:absolute;right:8px;top:10px;width:18px;height:18px;border-radius:50%;background:var(--gold)}

  /* probiotic jars */
  .jar{position:absolute;top:620px;width:128px;height:232px}
  .jar__lid{position:absolute;left:6px;top:0;width:116px;height:48px;background:var(--amber);border-radius:8px}
  .jar__body{position:absolute;left:0;top:44px;width:128px;height:188px;background:var(--amber);border-radius:10px;overflow:hidden}
  .jar__label{position:absolute;left:0;right:0;top:18px;height:150px}
  .jar__label--teal{background:var(--teal)}
  .jar__label--pink{background:var(--pink)}
  .jar .mini-name{font-size:15px}
  .strain{position:absolute;left:8px;top:92px;font-weight:800;font-size:11px;color:var(--brown);background:var(--white);padding:1px 5px}
  .jar .mini-copy{top:114px;width:100px}
</style>
</head>
<body>

  <!-- Poise Paste, front -->
  <section class="tube tube--teal" style="left:70px">
    <div class="tube__shoulder"></div>
    <div class="tube__pattern" role="img" aria-label="Checkered brown pattern band"></div>
    <div class="seal" role="img" aria-label="Quality seal"></div>
    <div class="brand">VELTRIX</div>
    <h2 class="product-name">Poise<br>Paste</h2>
    <p class="tagline">Tooth &amp; Gum Cleaning.</p>
    <ul class="features">
      <li>With</li>
      <li>Whitening Agents</li>
      <li>To Ensure</li>
      <li>Your Teeth Look</li>
      <li>Whiter &amp; Cleaner</li>
    </ul>
    <p class="net">100g <small>NET</small></p>
    <div class="tube__crimp"></div>
  </section>

  <!-- Poise Paste, back -->
  <section class="tube tube--teal" style="left:336px;width:250px">
    <div class="tube__shoulder"></div>
    <div class="tube__pattern tube__pattern--back" role="img" aria-label="Checkered brown pattern band"></div>
    <div class="back-copy" style="left:120px;top:250px;width:110px">
      <h3>HOW TO USE POISE TOOTHPASTE</h3>
      <p>Brush teeth and gums gently for two minutes, twice daily. Use a pea sized amount on a soft brush. Rinse mouth lightly afterwards. Follow with tongue gel for best results. Store below 30°C. Keep out of reach of children. Do not swallow.</p>
    </div>
    <div class="tube__crimp"></div>
  </section>

  <!-- Tongue Gel, front -->
  <section class="tube tube--pink" style="left:600px">
    <div class="tube__shoulder"></div>
    <div class="tube__pattern" role="img" aria-label="Checkered brown pattern band"></div>
    <div class="seal" role="img" aria-label="Quality seal"></div>
    <div class="brand">VELTRIX</div>
    <h2 class="product-name">Tongue<br>Gel</h2>
    <p class="tagline">Tongue Surface Cleaning.</p>
    <ul class="features" style="width:170px">
      <li>Non Abrasive Product.</li>
      <li>Contains Fluoride &amp;</li>
      <li>Chlorhexidine</li>
      <li>Do Use Gel As Both</li>
      <li>As A Toothpaste</li>
      <li>(Cleanse)</li>
    </ul>
    <p class="net">110g <small>NET</small></p>
    <div class="tube__crimp"></div>
  </section>

  <!-- Tongue Gel, back -->
  <section class="tube tube--pink" style="left:868px;width:270px">
    <div class="tube__shoulder"></div>
    <div class="tube__pattern tube__pattern--back" role="img" aria-label="Checkered brown pattern band"></div>
    <div class="back-copy" style="left:130px;top:240px;width:115px">
      <h3>HOW TO USE VELTRIX TONGUE GEL</h3>
      <p>Apply a small amount to the tongue cleaner. Scrape gently from back to front. Rinse cleaner after each stroke. Use morning and night after brushing. Avoid eating for thirty minutes.</p>
    </div>
    <div class="tube__crimp"></div>
  </section>

  <!-- Poise Rinse 1 -->
  <section class="bottle" style="left:190px">
    <div class="bottle__cap"></div>
    <div class="bottle__body">
      <div class="bottle__label bottle__label--teal">
        <div class="mini-brand">VELTRIX</div>
        <div class="mini-seal" role="img" aria-label="Quality seal"></div>
        <h3 class="mini-name">Poise<br>Rinse 1</h3>
        <p class="mini-copy">Mix equal parts of Rinse 1 and Rinse 2 before use.</p>
        <p class="mini-net">50ml e</p>
      </div>
    </div>
  </section>

  <!-- Poise Rinse 2 -->
  <section class="bottle" style="left:322px">
    <div class="bottle__cap"></div>
    <div class="bottle__body">
      <div class="bottle__label bottle__label--pink">
        <div class="mini-brand">VELTRIX</div>
        <div class="mini-seal" role="img" aria-label="Quality seal"></div>
        <h3 class="mini-name">Poise<br>Rinse 2</h3>
        <p class="mini-copy">Mix equal parts of Rinse 1 and Rinse 2 before use.</p>
        <p class="mini-net">50ml e</p>
      </div>
    </div>
  </section>

  <!-- Mouthwash TORVA R47 -->
  <section class="jar" style="left:512px">
    <div class="jar__lid"></div>
    <div class="jar__body">
      <div class="jar__label jar__label--teal">
        <div class="mini-brand">VELTRIX</div>
        <div class="mini-seal" role="img" aria-label="Quality seal"></div>
        <h3 class="mini-name">Mouthwash</h3>
        <p class="strain" style="top:70px">TORVA R47</p>
        <p class="mini-copy" style="top:94px">Probiotic lozenges for fresh breath</p>
        <p class="mini-copy" style="top:122px;font-weight:700">zephyrline · 30 lozenges</p>
      </div>
    </div>
  </section>

  <!-- Mouthwash TORVA P63 -->
  <section class="jar" style="left:652px">
    <div class="jar__lid"></div>
    <div class="jar__body">
      <div class="jar__label jar__label--pink">
        <div class="mini-brand">VELTRIX</div>
        <div class="mini-seal" role="img" aria-label="Quality seal"></div>
        <h3 class="mini-name">Mouthwash</h3>
        <p class="strain" style="top:70px">TORVA P63</p>
        <p class="mini-copy" style="top:94px">Probiotic lozenges for oral health</p>
        <p class="mini-copy" style="top:122px;font-weight:700">dentisafe · 30 lozenges</p>
      </div>
    </div>
  </section>

</body>
</html>
```